Tarvel Engineering Rail Sector Brochure

We need a new 3 page folding brochure for Tarvel Engineering Pty Ltd. The organisation is currently supporting customers in Defence, Maritime and Information and Communications Technology companies. We are currently looking to expand our engineering services into the rail sector by providing manpower and consultancy services to railway sector clients.We would like the brochure to be based on an A4 page and look technical with particular focus on communications systems used within the railways. This could include pictures of rail control centres, trains (Australian trains only please), train radio communications equipment, radio antennas, computers and networking equipment. Please use both graphics and photos.The brochure will be provided to potential rail customers and should be clear and uncluttered.The following is our company website: www.tarvelengineering-example.com.au if you would like more detail on our current work.I have attached the file for our logo which should appear on the brochure.
Target Market(s)
Providing manpower and consultancy services to the railway sector. This includes rail companies (e.g. Quillan Loop Transit, K/Rail etc) and rail equipment and carriage suppliers (e.g. Harvenko)
Colors
Designer to choose colors to be used in the design.
Requirements
Must have
- Instead of having "lorem ipsum" text in the brochure you can please use some of the text in the file we have provided. Not all has to be used, and you should not be limited to what is in the file.
Nice to have
- Mixture of different font sizes to highlight particular text elements.

```html
<!DOCTYPE html>
<html lang="en">
<head>
<meta charset="utf-8">
<title>Tarvel Engineering – Rail Sector Brochure</title>
<link rel="stylesheet" href="https://fonts.googleapis.com/css2?family=Open+Sans:wght@400;600;700&family=Oswald:wght@500&display=swap">
<style>
  :root {
    --page-bg: #d9d9db;
    --blue-deep: #1c45a8;
    --blue-main: #2a5bd0;
    --blue-light: #5a9ae8;
    --charcoal: #3a3a3c;
    --grey-mid: #6b6b6e;
    --grey-logo: #6d6e71;
    --white: #ffffff;
    --photo-dark: #1d2740;
    --photo-mid: #5d7fb0;
    --sky: #8fc4ec;
    --earth: #b36a3a;
  }
  * { margin: 0; padding: 0; box-sizing: border-box; }
  html, body { width: 902px; height: 1200px; overflow: hidden; }
  body {
    background: var(--page-bg);
    font-family: "Open Sans", Arial, sans-serif;
    position: relative;
  }
  .brochure {
    position: absolute;
    left: 16px; top: 290px;
    width: 870px; height: 621px;
    display: flex;
    box-shadow: 0 6px 18px rgba(0,0,0,.25);
  }
  .panel { position: relative; height: 100%; overflow: hidden; }
  .panel svg.backdrop { position: absolute; inset: 0; }

  /* About panel */
  .panel-about { width: 295px; }
  .about-content { position: absolute; left: 31px; right: 22px; top: 302px; color: var(--white); }
  .about-title { font-size: 14px; font-weight: 600; letter-spacing: .3px; margin-bottom: 10px; }
  .about-body p { font-size: 9.4px; line-height: 12.1px; text-align: justify; margin-bottom: 6px; }
  .visit-label { position: absolute; left: 0; right: 0; top: 536px; text-align: center; color: var(--white); font-size: 10px; font-weight: 600; }
  .web-box {
    position: absolute; left: 16px; top: 554px; width: 266px; height: 28px;
    background: var(--white); color: #333; font-size: 12.3px; font-weight: 600;
    display: flex; align-items: center; justify-content: center;
  }

  /* Contact panel */
  .panel-contact { width: 287px; }
  .contact-content { position: absolute; left: 0; right: 0; top: 358px; text-align: center; color: var(--white); }
  .brand-mark { display: inline-flex; align-items: center; gap: 7px; }
  .brand-mark .dot { width: 16px; height: 16px; border-radius: 50%; background: var(--white); }
  .brand-mark .name { font-size: 19px; font-weight: 600; }
  .brand-sub { font-size: 5.5px; margin-top: 3px; opacity: .85; }
  .office-title { color: var(--blue-light); font-size: 10.5px; font-weight: 600; margin-top: 26px; }
  .office-line { font-size: 9px; line-height: 12px; margin-top: 6px; }
  .contact-label { color: var(--blue-light); font-size: 8.5px; margin-top: 10px; }
  .contact-line { font-size: 8.5px; display: flex; justify-content: center; align-items: center; gap: 5px; }
  .icon { width: 9px; height: 9px; }

  /* Cover panel */
  .panel-cover { width: 288px; }
  .cover-brand { position: absolute; left: 0; right: 0; top: 70px; text-align: center; }
  .cover-brand .brand-mark .dot { background: var(--blue-main); width: 22px; height: 22px; }
  .cover-brand .brand-mark .name { color: var(--grey-logo); font-size: 24px; font-weight: 600; }
  .cover-brand .brand-sub { color: #333; font-size: 5.8px; }
  .tagline {
    position: absolute; left: 0; right: 0; top: 508px; text-align: center;
    font-family: "Oswald", "Arial Narrow", sans-serif; font-weight: 500;
    color: var(--white); font-size: 27px; line-height: 40px; letter-spacing: .2px;
  }
</style>
</head>
<body>
<div class="brochure">

  <section class="panel panel-about">
    <svg class="backdrop" width="295" height="621" viewBox="0 0 295 621">
      <defs>
        <linearGradient id="aboutBlue" x1="0" y1="0" x2="0" y2="1">
          <stop offset="0" stop-color="#2f62d6"/><stop offset="1" stop-color="#1b44a6"/>
        </linearGradient>
        <linearGradient id="techPhoto" x1="0" y1="0" x2="1" y2="1">
          <stop offset="0" stop-color="#1a1f2e"/><stop offset=".55" stop-color="#3f5f8e"/><stop offset="1" stop-color="#a9c6e4"/>
        </linearGradient>
      </defs>
      <rect width="295" height="621" fill="url(#aboutBlue)"/>
      <circle cx="190" cy="-40" r="300" fill="none" stroke="var(--blue-main)" stroke-width="18"/>
      <circle cx="160" cy="-30" r="290" fill="var(--white)"/>
      <circle cx="150" cy="-40" r="283" fill="url(#techPhoto)" role="img" aria-label="Photo of hands holding a laptop, tablet and phone around a glowing network globe"/>
    </svg>
    <div class="about-content">
      <h2 class="about-title">ABOUT US</h2>
      <div class="about-body">
        <p>At Tarvel Engineering we have a broad mix of capabilities, including abilities in the areas of networking, communications, C2 system integration with sensor and communications systems. Our staff have supported the largest telecommunications networks in Australia and aided defence in building real-time, secure data networks for communications and data sharing. We have enabled communications across multiple platforms types including aircraft, rail, ship and vehicle platforms that operate reliably under extreme environmental conditions.</p>
        <p>At Tarvel Engineering, we are committed to delivering value to all our customers and end users in a manner that inspires.</p>
      </div>
    </div>
    <p class="visit-label">Visit Us for more information</p>
    <div class="web-box">www.tarvelengineering-example.com.au</div>
  </section>

  <section class="panel panel-contact">
    <svg class="backdrop" width="287" height="621" viewBox="0 0 287 621">
      <defs>
        <linearGradient id="contactGrey" x1="0" y1="0" x2="1" y2="0">
          <stop offset="0" stop-color="#2e2e30"/><stop offset=".6" stop-color="#4a4a4d"/><stop offset="1" stop-color="#707073"/>
        </linearGradient>
      </defs>
      <rect width="287" height="621" fill="url(#contactGrey)"/>
    </svg>
    <div class="contact-content">
      <div class="brand-mark"><span class="dot"></span><span class="name">Tarvel Engineering</span></div>
      <p class="brand-sub">Command • Control • Communications • Computers</p>
      <p class="office-title">MAIN OFFICE ADDRESS:</p>
      <p class="office-line">
        <svg class="icon" viewBox="0 0 10 10"><path d="M5 0.5a3 3 0 0 1 3 3c0 2.3-3 6-3 6s-3-3.7-3-6a3 3 0 0 1 3-3z" fill="var(--white)"/><circle cx="5" cy="3.5" r="1.1" fill="var(--charcoal)"/></svg>
        Level 4, 18 Carrow St<br>Eastvale 3000
      </p>
      <p class="contact-label">Career Opportunities:</p>
      <p class="contact-line"><svg class="icon" viewBox="0 0 10 10"><rect x="0.5" y="2" width="9" height="6" fill="var(--white)"/><path d="M0.5 2l4.5 3.5 4.5-3.5" fill="none" stroke="var(--charcoal)" stroke-width=".8"/></svg>jobs@tarvelengineering-example.com.au</p>
      <p class="contact-label">General Enquiries:</p>
      <p class="contact-line"><svg class="icon" viewBox="0 0 10 10"><rect x="0.5" y="2" width="9" height="6" fill="var(--white)"/><path d="M0.5 2l4.5 3.5 4.5-3.5" fill="none" stroke="var(--charcoal)" stroke-width=".8"/></svg>info@tarvelengineering-example.com.au</p>
    </div>
  </section>

  <section class="panel panel-cover">
    <svg class="backdrop" width="288" height="621" viewBox="0 0 288 621">
      <defs>
        <linearGradient id="coverWhite" x1="0" y1="0" x2="1" y2="0">
          <stop offset="0" stop-color="#d6d6d8"/><stop offset=".15" stop-color="#ffffff"/><stop offset="1" stop-color="#ffffff"/>
        </linearGradient>
        <linearGradient id="coverBlue" x1="0" y1="0" x2="1" y2="1">
          <stop offset="0" stop-color="#3a72e0"/><stop offset="1" stop-color="#1b44a6"/>
        </linearGradient>
        <linearGradient id="trainPhoto" x1="0" y1="0" x2="0" y2="1">
          <stop offset="0" stop-color="var(--sky)"/><stop offset=".55" stop-color="#e3c23a"/><stop offset="1" stop-color="var(--earth)"/>
        </linearGradient>
        <linearGradient id="operatorPhoto" x1="0" y1="0" x2="1" y2="1">
          <stop offset="0" stop-color="#c9cfd6"/><stop offset="1" stop-color="#3b4250"/>
        </linearGradient>
      </defs>
      <rect width="288" height="621" fill="url(#coverWhite)"/>
      <path d="M0 470 C60 500 200 440 288 300 L288 621 L0 621 Z" fill="url(#coverBlue)"/>
      <path d="M230 240 A135 135 0 1 0 250 400" fill="none" stroke="var(--blue-main)" stroke-width="26"/>
      <circle cx="128" cy="330" r="106" fill="var(--white)"/>
      <circle cx="128" cy="330" r="100" fill="url(#trainPhoto)" role="img" aria-label="Photo of a yellow and blue freight locomotive on a red-earth rail line"/>
      <circle cx="68" cy="428" r="66" fill="var(--white)"/>
      <circle cx="68" cy="428" r="61" fill="url(#operatorPhoto)" role="img" aria-label="Photo of a rail operator in a cap speaking into a handheld radio"/>
    </svg>
    <div class="cover-brand">
      <div class="brand-mark"><span class="dot"></span><span class="name">Tarvel Engineering</span></div>
      <p class="brand-sub">Command • Control • Communications • Computers</p>
    </div>
    <h1 class="tagline">SMART SOLUTIONS THAT<br>DELIVER EXCELLENCE</h1>
  </section>

</div>
</body>
</html>
```